Delmer's Pressure Washing Services

Starting a pressure washing business on my own in Central Valley California, not too much experience so affordable, I do houses, fences, driveways, cars, trailers, RVs. Planning to make this full-time hoping clientele picks up after having a nice business card. Design doesn't have to be flashy, more to the point, I like simplistic/personable. I do not want something exhausting to look at or with too much going on.

Target Market(s)

Residential, Commercial

Industry/Entity Type

Pressure Washing

Contact Information for Business Card

avalible Services

Font styles to use
Sans Serif

Colors
0054AA
0677BA
7BADD7
CADEEF
E8F1F8
0094D4
00A9DD
6FCCEA
C7EBF8
E9F6FB
00AB8E
00BBA5
67D7C9
C6EFE9
E9F9F6

```html
<!DOCTYPE html>
<html lang="en">
<head>
<meta charset="utf-8">
<title>Delmer's Pressure Washing Services – Business Card</title>
<link href="https://fonts.googleapis.com/css2?family=Roboto:wght@400;500;700&display=swap" rel="stylesheet">
<style>
  :root {
    --backdrop: #3a3a3a;
    --teal: #00bba5;
    --teal-deep: #00ab8e;
    --blue: #0677ba;
    --blue-deep: #0054aa;
    --white: #ffffff;
    --shadow: rgba(0,0,0,0.85);
  }
  * { box-sizing: border-box; margin: 0; padding: 0; }
  html, body {
    width: 1075px; height: 1200px; overflow: hidden;
    background: var(--backdrop);
    font-family: "Roboto", Arial, sans-serif;
  }
  .card {
    position: absolute;
    width: 663px; height: 395px;
    box-shadow: 3px 3px 2px var(--shadow);
    overflow: hidden;
  }
  .card-front { left: 206px; top: 187px; background: var(--teal); }
  .card-back { left: 203px; top: 637px; background: var(--white); }
  .front-art { position: absolute; inset: 0; }
  .contact-block { position: absolute; left: 36px; top: 0; color: var(--white); }
  .person-name {
    position: absolute; top: 144px; left: 0; white-space: nowrap;
    font-weight: 700; font-size: 24px; letter-spacing: 0.2px;
  }
  .person-role {
    position: absolute; top: 172px; left: 0; white-space: nowrap;
    font-size: 18px;
  }
  .address {
    position: absolute; top: 210px; left: 0; white-space: nowrap;
    font-size: 18px; line-height: 23px;
  }
  .contact-list {
    position: absolute; top: 279px; left: 0; list-style: none;
    font-size: 18px; line-height: 23.5px; white-space: nowrap;
  }
  .contact-list li { display: flex; align-items: center; gap: 6px; }
  .contact-list svg { width: 17px; height: 17px; flex: none; }
  .wordmark {
    position: absolute; left: 0; right: 0; top: 163px;
    display: flex; align-items: center; justify-content: center; gap: 18px;
  }
  .wordmark-dot { width: 62px; height: 62px; border-radius: 50%; background: var(--teal); flex: none; }
  .wordmark-name {
    color: var(--teal); font-weight: 500; font-size: 26px; line-height: 32px;
    text-transform: uppercase; letter-spacing: 1px;
  }
</style>
</head>
<body>
  <section class="card card-front">
    <svg class="front-art" width="663" height="395" viewBox="0 0 663 395">
      <polygon role="img" aria-label="Illustration area: pressure washer wand spraying water" points="90,0 663,0 663,395" fill="var(--blue)"/>
    </svg>
    <div class="contact-block">
      <div class="person-name">MARCUS DELGADO</div>
      <div class="person-role">Managing Director</div>
      <div class="address">1187 Orchard Lane, Fresno<br>93721, United States</div>
      <ul class="contact-list">
        <li><svg viewBox="0 0 24 24"><path fill="var(--white)" d="M6.6 10.8a15.1 15.1 0 0 0 6.6 6.6l2.2-2.2a1 1 0 0 1 1-.25 11.4 11.4 0 0 0 3.6.57 1 1 0 0 1 1 1V20a1 1 0 0 1-1 1A17 17 0 0 1 3 4a1 1 0 0 1 1-1h3.5a1 1 0 0 1 1 1c0 1.25.2 2.45.57 3.6a1 1 0 0 1-.25 1z"/></svg>559-204 318 776</li>
        <li><svg viewBox="0 0 24 24"><rect x="2" y="5" width="20" height="14" fill="var(--white)"/><path d="M2 5l10 8 10-8" stroke="var(--teal)" stroke-width="1.6" fill="none"/></svg>hello@delmerswash.com</li>
        <li><svg viewBox="0 0 24 24" fill="none" stroke="var(--white)" stroke-width="1.8"><circle cx="12" cy="12" r="9.5"/><ellipse cx="12" cy="12" rx="4" ry="9.5"/><path d="M2.5 12h19M4 7h16M4 17h16"/></svg>www.delmerswash.com</li>
      </ul>
    </div>
  </section>

  <section class="card card-back">
    <div class="wordmark">
      <span class="wordmark-dot"></span>
      <span class="wordmark-name">Delmer's<br>Pressure Washing Services</span>
    </div>
  </section>
</body>
</html>
```